New website design and logo for FusoBrite.com to help ignite the website sales.

Hi designers,

Fusobrite is a new welding brand that is selling welding equipement.

Currently I have around 5 to 10 products. The issue is that the site itself does not do that much of sales. So I have to do something about the seo etc. but that is out of scope for the design.

What is in scope is to comeup with a new logo and website look and feel that is in line with the customers.

men, non professionals, garage, home improvements, perhaps sme ( small mediul entreprice business that want to start in the welding industry.

Products are midrange prices and quality. The look and feel must breath cool stuff, sexy ( women in working cloths carrying welding gloves, other protection gear and weldels)

The wedsite is build in wordpress with the Divi theme. I am an IT guy myself withhout any creativity in me :( so if you can help me with that that would be great.

Please have a quick look at fusobrite.com

Best regards,
Joost

Target Market(s)

non professional welders that do metal work in there garage

Coding

Coded - Design and coding required

Number of Pages Required

3 page

Font styles to use
Sans Serif

Colors
0355a3
ffc214

Requirements
Must have
• I would like to see a new homepage and product page design together with a new logo.
Nice to have
• shop design

```html
<!DOCTYPE html>
<html lang="en">
<head>
<meta charset="utf-8">
<title>Fusobrite – Homepage Design</title>
<link href="https://fonts.googleapis.com/css2?family=Montserrat:wght@300;400;500;600;700&display=swap" rel="stylesheet">
<style>
:root{
  --blue:#0370d0;
  --blue-deep:#0355a3;
  --yellow:#ffc214;
  --dark:#1c1d20;
  --darker:#141517;
  --grey-bg:#e3e3e5;
  --white:#ffffff;
  --text:#2a2a2a;
  --muted:#8a8a8a;
}
*{box-sizing:border-box;margin:0;padding:0}
html,body{width:1200px;height:2594px;overflow:hidden}
body{font-family:'Montserrat',sans-serif;background:var(--grey-bg);position:relative;color:var(--text)}
.abs{position:absolute}
.stage-top{left:0;top:0;width:1200px;height:640px;background:var(--white);clip-path:polygon(0 0,100% 0,100% 580px,50% 490px,0 580px)}
.brand-mark{left:0;top:92px;width:1200px;display:flex;justify-content:center;align-items:center;gap:12px}
.brand-dot{width:40px;height:40px;border-radius:50%;background:var(--yellow)}
.brand-name{font-size:34px;font-weight:700;color:var(--blue-deep);letter-spacing:1px}

.btn{display:inline-flex;align-items:center;justify-content:center;gap:6px;background:var(--yellow);color:var(--text);font-weight:700;border-radius:2px;white-space:nowrap}
.btn svg{stroke:var(--text);fill:none}

/* Laptop screen */
.screen{left:247px;top:296px;width:706px;height:442px;overflow:hidden;background:linear-gradient(135deg,#0e1a2e 0%,#1f3a5e 45%,#0b1220 100%)}
.screen .photo{position:absolute;inset:0;background:radial-gradient(circle at 72% 72%,rgba(255,190,90,.55),rgba(40,60,90,.2) 30%,transparent 55%),linear-gradient(160deg,#0a1322,#23406a 55%,#0a0f18)}
.screen-topbar{position:absolute;left:0;top:0;width:706px;height:26px;background:var(--blue);display:flex;align-items:center;font-size:7px;color:#cfe0f5}
.screen-search{margin-left:74px;display:flex;align-items:center;gap:6px}
.screen-phone{position:absolute;right:74px;top:5px;height:21px;width:118px;background:var(--yellow);color:var(--text);font-weight:700;font-size:7px;display:flex;align-items:center;justify-content:center;gap:5px}
.screen-nav{position:absolute;left:73px;top:26px;width:560px;height:48px;background:var(--white);display:flex;align-items:center;font-size:7px}
.nav-links{display:flex;gap:24px;margin-left:48px}
.nav-links .active{font-weight:700;border-bottom:1px solid var(--text);padding-bottom:2px}
.nav-logo{position:absolute;left:50%;transform:translateX(-50%);display:flex;align-items:center;gap:4px;font-weight:700;color:var(--blue-deep)}
.nav-logo .d{border-radius:50%;background:var(--yellow)}
.nav-right{position:absolute;right:36px;display:flex;gap:16px;align-items:center}
.nav-right span{display:flex;align-items:center;gap:4px}
.screen-headline{position:absolute;left:0;top:174px;width:706px;text-align:center;color:var(--white);font-size:31px;line-height:30px;font-weight:500}
.screen .btn{position:absolute;left:301px;top:294px;width:104px;height:26px;font-size:7px}
.screen-chev{position:absolute;left:343px;top:416px}
.screen-corner{position:absolute;bottom:0;width:706px;height:20px}

/* labels */
.label{top:900px;font-size:13px;letter-spacing:9px;color:var(--text);font-weight:500}

/* Desktop */
.desk{left:94px;top:946px;width:706px;height:1517px;background:var(--white);overflow:hidden}
.d-topbar{position:absolute;left:0;top:0;width:706px;height:20px;background:var(--dark);font-size:6px;color:#999;display:flex;align-items:center}
.d-topbar .screen-search{margin-left:74px}
.d-phone{position:absolute;left:514px;top:0;height:20px;width:118px;background:var(--yellow);color:var(--text);font-weight:700;font-size:7px;display:flex;align-items:center;justify-content:center;gap:5px}
.d-nav{position:absolute;left:0;top:20px;width:706px;height:46px;border-bottom:1px solid #ececec;display:flex;align-items:center;font-size:7px}
.d-nav .nav-links{margin-left:74px;gap:24px}
.d-nav .nav-right{right:74px}
.tile{position:absolute;overflow:hidden}
.tile-title{position:absolute;color:var(--white);font-weight:300}
.tile .btn{position:absolute;height:24px;font-size:7px;width:106px}
.ship-band{position:absolute;left:0;top:440px;width:706px;height:177px;background:linear-gradient(90deg,var(--blue) 60%,#1a7fd8)}
.ship-box{position:absolute;background:var(--white);display:flex;align-items:center;justify-content:center;gap:18px;color:var(--text)}
.prod-sec{position:absolute;left:0;top:617px;width:706px;height:759px;background:var(--dark)}
.prod-title{position:absolute;left:74px;top:46px;font-size:30px;color:var(--white);font-weight:500}
.prod{position:absolute;width:130px}
.prod .img{width:130px;height:166px;background:var(--white);display:flex;align-items:center;justify-content:center}
.prod .img div{width:80px;height:110px;border-radius:8px}
.prod .name{color:var(--white);font-size:6.5px;font-weight:600;margin-top:10px;height:30px;line-height:8px}
.prod .price{color:var(--yellow);font-size:11px}
.rule{position:absolute;left:74px;width:556px;height:1px;background:#444}
.d-footer{position:absolute;left:0;top:1376px;width:706px;height:141px;background:var(--white)}
.foot-links{position:absolute;left:74px;top:40px;font-size:7px;color:#444;display:flex;gap:10px}
.copy{position:absolute;font-size:6.5px;color:#555}
.socials{position:absolute;display:flex}
.socials span{border-radius:50%;display:block}

/* Mobile */
.mob{left:922px;top:946px;width:184px;height:1214px;background:var(--white);overflow:hidden}
.m-topbar{position:absolute;left:0;top:0;width:184px;height:17px;background:var(--dark)}
.m-phone{position:absolute;left:75px;top:0;width:98px;height:17px;background:var(--yellow);font-size:6px;font-weight:700;display:flex;align-items:center;justify-content:center;gap:3px}
.m-nav{position:absolute;left:0;top:17px;width:184px;height:33px;border-bottom:1px solid #eee}
.mob .tile-title{font-size:20px}
.mob .btn{width:74px;height:16px;font-size:5px}
.m-footer-links{position:absolute;left:0;top:1082px;width:184px;text-align:center;font-size:5.5px;line-height:9.5px;color:#555}
</style>
</head>
<body>

<div class="abs stage-top"></div>

<div class="abs brand-mark">
  <span class="brand-dot"></span>
  <span class="brand-name">FUSOBRITE</span>
</div>

<!-- Homepage hero, full screen view -->
<section class="abs screen">
  <div class="photo" role="img" aria-label="Welder in protective helmet working with sparks flying"></div>
  <div class="screen-topbar">
    <div class="screen-search">
      <svg width="8" height="8" viewBox="0 0 10 10" fill="none" stroke="#fff" stroke-width="1.4"><circle cx="4" cy="4" r="3"/><path d="M6.3 6.3 9 9"/></svg>
      Search it here....
    </div>
    <div class="screen-phone">
      <svg width="8" height="8" viewBox="0 0 10 10"><path d="M2 1l2 2-1 1.2c.6 1.3 1.5 2.2 2.8 2.8L7 6l2 2-1.3 1.3C4.5 9 1 5.5.7 2.3z" fill="#222"/></svg>
      +31(0)612345678
    </div>
  </div>
  <nav class="screen-nav">
    <div class="nav-links"><span class="active">Home</span><span>products</span><span>Contact us</span></div>
    <div class="nav-logo"><span class="d" style="width:14px;height:14px"></span>FUSOBRITE</div>
    <div class="nav-right">
      <span><svg width="9" height="9" viewBox="0 0 10 10" fill="none" stroke="#0370d0"><path d="M1 3h8l-1 6H2z"/><path d="M3.5 3V1.5h3V3"/></svg>2</span>
      <span><svg width="9" height="9" viewBox="0 0 10 10" fill="none" stroke="#0370d0"><circle cx="5" cy="3" r="2"/><path d="M1 9.5c0-2.5 2-3.5 4-3.5s4 1 4 3.5"/></svg>My account</span>
    </div>
  </nav>
  <h1 class="screen-headline">Simple welding of steel and<br>aluminum Get great results with<br>tools that work</h1>
  <a class="btn">Shop Now <svg width="14" height="6" viewBox="0 0 14 6"><path d="M0 3h13M10 .5 13 3l-3 2.5"/></svg></a>
  <svg class="screen-chev" width="20" height="22" viewBox="0 0 20 22" fill="none" stroke="#fff" stroke-width="3"><path d="M3 3l7 7 7-7M3 11l7 7 7-7"/></svg>
  <svg class="screen-corner" viewBox="0 0 706 20" preserveAspectRatio="none"><path d="M0 4 L240 20 L0 20Z" fill="#fff"/><path d="M706 4 L466 20 L706 20Z" fill="#fff"/><path d="M0 2 L240 20" stroke="#0370d0" stroke-width="2"/><path d="M706 2 L466 20" stroke="#0370d0" stroke-width="2"/></svg>
</section>

<div class="abs label" style="left:386px">DESKTOP</div>
<div class="abs label" style="left:964px">MOBILE</div>

<!-- Desktop homepage -->
<main class="abs desk">
  <div class="d-topbar">
    <div class="screen-search">
      <svg width="8" height="8" viewBox="0 0 10 10" fill="none" stroke="#ccc" stroke-width="1.4"><circle cx="4" cy="4" r="3"/><path d="M6.3 6.3 9 9"/></svg>
      Search it here....
    </div>
    <div class="d-phone">
      <svg width="8" height="8" viewBox="0 0 10 10"><path d="M2 1l2 2-1 1.2c.6 1.3 1.5 2.2 2.8 2.8L7 6l2 2-1.3 1.3C4.5 9 1 5.5.7 2.3z" fill="#222"/></svg>
      +31(0)612345678
    </div>
  </div>
  <nav class="d-nav">
    <div class="nav-links"><span class="active" style="border-bottom-color:var(--blue)">Home</span><span>products</span><span>Contact us</span></div>
    <div class="nav-logo" style="left:353px"><span class="d" style="width:16px;height:16px"></span>FUSOBRITE</div>
    <div class="nav-right">
      <span><svg width="9" height="9" viewBox="0 0 10 10" fill="none" stroke="#0370d0"><path d="M1 3h8l-1 6H2z"/><path d="M3.5 3V1.5h3V3"/></svg>2</span>
      <span><svg width="9" height="9" viewBox="0 0 10 10" fill="none" stroke="#0370d0"><circle cx="5" cy="3" r="2"/><path d="M1 9.5c0-2.5 2-3.5 4-3.5s4 1 4 3.5"/></svg>My account</span>
    </div>
  </nav>

  <div class="tile" style="left:12px;top:78px;width:335px;height:350px;background:linear-gradient(160deg,#5a4a3c,#2a2622 55%,#151413)" role="img" aria-label="Welder in helmet with glowing visor at work">
    <div class="tile-title" style="left:36px;top:206px;font-size:18px;line-height:18.5px;font-weight:500">Simple welding of steel and<br>aluminum Get great results<br>with tools that work</div>
    <a class="btn" style="left:36px;top:285px">Shop Now <svg width="14" height="6" viewBox="0 0 14 6"><path d="M0 3h13M10 .5 13 3l-3 2.5"/></svg></a>
  </div>
  <div class="tile" style="left:359px;top:78px;width:335px;height:169px;background:linear-gradient(100deg,#2a2b2e 35%,#6b5c4e 70%,#c77b3a)" role="img" aria-label="Gloved hands welding with sparks">
    <div class="tile-title" style="left:36px;top:34px;font-size:44px">Gloves</div>
    <a class="btn" style="left:36px;top:100px">Shop Now <svg width="14" height="6" viewBox="0 0 14 6"><path d="M0 3h13M10 .5 13 3l-3 2.5"/></svg></a>
  </div>
  <div class="tile" style="left:359px;top:259px;width:335px;height:169px;background:linear-gradient(100deg,#3a3836 40%,#7a5a50 75%,#9e2b25)" role="img" aria-label="MIG welding machine on a workshop bench">
    <div class="tile-title" style="left:36px;top:34px;font-size:44px">Mig</div>
    <a class="btn" style="left:36px;top:100px">Shop Now <svg width="14" height="6" viewBox="0 0 14 6"><path d="M0 3h13M10 .5 13 3l-3 2.5"/></svg></a>
  </div>

  <section class="ship-band">
    <div class="ship-box" style="left:173px;top:46px;width:361px;height:85px;font-size:15px">
      <svg width="36" height="30" viewBox="0 0 36 30" fill="none" stroke="#ffc214" stroke-width="2"><rect x="2" y="4" width="20" height="18"/><path d="M22 10h7l5 6v6H22"/><circle cx="9" cy="24" r="3" fill="#fff"/><circle cx="27" cy="24" r="3" fill="#fff"/></svg>
      Free shipping from € 30.00
    </div>
  </section>

  <section class="prod-sec">
    <h2 class="prod-title">Our Products</h2>
    <div class="prod" style="left:74px;top:117px"><div class="img" role="img" aria-label="Red MIG-250P welding machine"><div style="background:linear-gradient(#d9452f,#3a2a28)"></div></div><p class="name">MIG-250P</p><p class="price">€ 795.00</p></div>
    <div class="prod" style="left:217px;top:117px"><div class="img" role="img" aria-label="Blue and white MIG-2500 welding machine"><div style="background:linear-gradient(90deg,#c9ccd2,#2f6fc4)"></div></div><p class="name">MIG-2500</p><p class="price">€ 745.00</p></div>
    <div class="prod" style="left:360px;top:117px"><div class="img" role="img" aria-label="Black welding helmet with purple visor"><div style="border-radius:40px;background:radial-gradient(circle at 40% 40%,#9a55d0 20%,#222 22%)"></div></div><p class="name">Welding helmet 180 degrees view</p><p class="price">€ 109.00</p></div>
    <div class="prod" style="left:502px;top:117px"><div class="img" role="img" aria-label="Large black measuring triangle"><div style="background:linear-gradient(135deg,transparent 50%,#222 50%)"></div></div><p class="name">Large measuring triangle | 12 inches | speed square | square | measuring tool</p><p class="price">€ 25.00</p></div>
    <div class="rule" style="top:367px"></div>
    <div class="prod" style="left:74px;top:397px"><div class="img" role="img" aria-label="Black leather welding gloves"><div style="background:linear-gradient(#3a3a32,#1f1f1c)"></div></div><p class="name">Welding gloves Black</p><p class="price">€ 22.40</p></div>
    <div class="prod" style="left:217px;top:397px"><div class="img" role="img" aria-label="Black welding helmet with large view"><div style="border-radius:40px;background:radial-gradient(circle at 40% 45%,#a05ad6 22%,#222 24%)"></div></div><p class="name">Welding helmet large view</p><p class="price">€ 89.00</p></div>
    <div class="prod" style="left:360px;top:397px"><div class="img" role="img" aria-label="Small black measuring triangle"><div style="background:linear-gradient(135deg,transparent 50%,#222 50%)"></div></div><p class="name">Small measuring triangle | 7 inches | speed square | square | measuring tool</p><p class="price">€ 17.25</p></div>
    <div class="prod" style="left:502px;top:397px"><div class="img" role="img" aria-label="Blue welding gloves with yellow cuffs"><div style="background:linear-gradient(#1e4bc0,#f0b21a 60%,#1e4bc0)"></div></div><p class="name">Welding gloves Blue</p><p class="price">€ 22.40</p></div>
    <div class="rule" style="top:643px"></div>
    <a class="btn" style="position:absolute;left:74px;top:672px;width:129px;height:28px;font-size:7px">View all products <svg width="14" height="6" viewBox="0 0 14 6"><path d="M0 3h13M10 .5 13 3l-3 2.5"/></svg></a>
  </section>

  <footer class="d-footer">
    <div class="foot-links"><span>Home</span>|<span>products</span>|<span>Customer care</span>|<span>Information</span>|<span>Sources</span></div>
    <p class="copy" style="left:74px;top:56px">Copyright © 2021. Fusobrite - All Rights Reserved.</p>
    <div class="socials" style="left:74px;top:77px;gap:8px" aria-label="Social media links">
      <span style="width:24px;height:24px;background:#3b5998"></span>
      <span style="width:24px;height:24px;background:#d6336c"></span>
      <span style="width:24px;height:24px;background:#0a66c2"></span>
    </div>
    <div style="position:absolute;left:489px;top:24px;width:1px;height:90px;background:#e5e5e5"></div>
    <div style="position:absolute;left:540px;top:56px;display:flex;align-items:center;gap:6px;font-weight:700;font-size:15px;color:var(--blue-deep)"><span style="width:20px;height:20px;border-radius:50%;background:var(--yellow)"></span>FUSOBRITE</div>
  </footer>
</main>

<!-- Mobile homepage -->
<main class="abs mob">
  <div class="m-topbar">
    <svg style="position:absolute;left:9px;top:4px" width="8" height="8" viewBox="0 0 10 10" fill="none" stroke="#ccc" stroke-width="1.4"><circle cx="4" cy="4" r="3"/><path d="M6.3 6.3 9 9"/></svg>
    <div class="m-phone"><svg width="6" height="6" viewBox="0 0 10 10"><path d="M2 1l2 2-1 1.2c.6 1.3 1.5 2.2 2.8 2.8L7 6l2 2-1.3 1.3C4.5 9 1 5.5.7 2.3z" fill="#222"/></svg>+31(0)612345678</div>
  </div>
  <nav class="m-nav">
    <svg style="position:absolute;left:9px;top:12px" width="18" height="8" viewBox="0 0 18 8" stroke="#444"><path d="M0 1h18M0 7h12"/></svg>
    <div style="position:absolute;left:72px;top:11px;display:flex;align-items:center;gap:3px;font-size:6px;font-weight:700;color:var(--blue-deep)"><span style="width:10px;height:10px;border-radius:50%;background:var(--yellow)"></span>FUSOBRITE</div>
    <svg style="position:absolute;left:152px;top:12px" width="8" height="8" viewBox="0 0 10 10" fill="none" stroke="#0370d0"><path d="M1 3h8l-1 6H2z"/></svg>
    <svg style="position:absolute;left:165px;top:12px" width="8" height="8" viewBox="0 0 10 10" fill="none" stroke="#0370d0"><circle cx="5" cy="3" r="2"/><path d="M1 9.5c0-2.5 2-3.5 4-3.5s4 1 4 3.5"/></svg>
  </nav>
  <div class="tile" style="left:9px;top:58px;width:167px;height:174px;background:linear-gradient(160deg,#5a4a3c,#2a2622 55%,#151413)" role="img" aria-label="Welder in helmet with glowing visor at work">
    <div class="tile-title" style="left:12px;top:94px;font-size:8.5px;line-height:9px;font-weight:500">Simple welding of steel and<br>aluminum Get great results<br>with tools that work</div>
    <a class="btn" style="left:12px;top:138px">Shop Now <svg width="9" height="5" viewBox="0 0 14 6"><path d="M0 3h13M10 .5 13 3l-3 2.5"/></svg></a>
  </div>
  <div class="tile" style="left:9px;top:242px;width:167px;height:98px;background:linear-gradient(100deg,#2a2b2e 35%,#6b5c4e 70%,#c77b3a)" role="img" aria-label="Gloved hands welding with sparks">
    <div class="tile-title" style="left:12px;top:18px">Gloves</div>
    <a class="btn" style="left:12px;top:54px">Shop Now <svg width="9" height="5" viewBox="0 0 14 6"><path d="M0 3h13M10 .5 13 3l-3 2.5"/></svg></a>
  </div>
  <div class="tile" style="left:9px;top:350px;width:167px;height:98px;background:linear-gradient(100deg,#2a2b2e 35%,#6b5c4e 70%,#c77b3a)" role="img" aria-label="Gloved hands holding welding gear">
    <div class="tile-title" style="left:12px;top:18px">Mig</div>
    <a class="btn" style="left:12px;top:54px">Shop Now <svg width="9" height="5" viewBox="0 0 14 6"><path d="M0 3h13M10 .5 13 3l-3 2.5"/></svg></a>
  </div>
  <section class="ship-band" style="top:458px;width:184px;height:164px">
    <div class="ship-box" style="left:9px;top:32px;width:167px;height:102px;flex-direction:column;gap:8px;font-size:11px;text-align:center;line-height:12px">
      <svg width="26" height="22" viewBox="0 0 36 30" fill="none" stroke="#ffc214" stroke-width="2"><rect x="2" y="4" width="20" height="18"/><path d="M22 10h7l5 6v6H22"/><circle cx="9" cy="24" r="3" fill="#fff"/><circle cx="27" cy="24" r="3" fill="#fff"/></svg>
      Free shipping from<br>€ 30.00
    </div>
  </section>
  <section class="prod-sec" style="top:622px;width:184px;height:362px">
    <h2 style="position:absolute;left:0;top:28px;width:184px;text-align:center;color:#fff;font-size:13px;font-weight:500">Our Products</h2>
    <div style="position:absolute;left:26px;top:68px;width:134px;height:170px;background:#fff;display:flex;align-items:center;justify-content:center" role="img" aria-label="Red MIG-250P welding machine"><div style="width:84px;height:110px;border-radius:8px;background:linear-gradient(#d9452f,#3a2a28)"></div></div>
    <p style="position:absolute;left:0;top:245px;width:184px;text-align:center;color:#fff;font-size:5.5px;font-weight:600">MIG-250P</p>
    <p style="position:absolute;left:0;top:256px;width:184px;text-align:center;color:var(--yellow);font-size:10px">€ 795.00</p>
    <div style="position:absolute;left:9px;top:289px;width:167px;height:1px;background:#444"></div>
    <div style="position:absolute;left:9px;top:288px;width:26px;height:3px;background:#fff"></div>
    <a class="btn" style="position:absolute;left:44px;top:309px;width:97px;height:20px;font-size:5px">View all products <svg width="9" height="5" viewBox="0 0 14 6"><path d="M0 3h13M10 .5 13 3l-3 2.5"/></svg></a>
  </section>
  <div style="position:absolute;left:0;top:1030px;width:184px;display:flex;justify-content:center;align-items:center;gap:4px;font-size:9px;font-weight:700;color:var(--blue-deep)"><span style="width:14px;height:14px;border-radius:50%;background:var(--yellow)"></span>FUSOBRITE</div>
  <div class="m-footer-links">Home<br>products<br>Customer care<br>Information<br>Sources</div>
  <p class="copy" style="left:0;top:1136px;width:184px;text-align:center;font-size:5px;line-height:9px">Copyright © 2021. Fusobrite - All Rights<br>Reserved.</p>
  <div class="socials" style="left:61px;top:1174px;gap:7px" aria-label="Social media links">
    <span style="width:16px;height:16px;background:#3b5998"></span>
    <span style="width:16px;height:16px;background:#d6336c"></span>
    <span style="width:16px;height:16px;background:#0a66c2"></span>
  </div>
</main>

</body>
</html>
```